Loan broker seeks referral card design for real estate financing

We need a design for a referral card for people who recommend us for real estate financing. If the deal goes through, each referrer will receive €750.

Text similar to: Recommend me! For every successful real estate financing referral, you will receive €750. (Other suggestions are also welcome)

The size should be no larger than A5 format, or possibly even oblong.
The design should convey security and competence and include themes such as independent advice.

The design should also include the company logo and a photo of me. Naturally, the design should also include a link to my website: www.die-brennholt.at, along with my phone number and email address: office@die-brennholt.at

```html
<!DOCTYPE html>
<html lang="de">
<head>
<meta charset="utf-8">
<title>Referral Card – Brennholt Finanzberatung</title>
<link rel="stylesheet" href="https://fonts.googleapis.com/css2?family=Outfit:wght@400;500;600;700;800&display=swap">
<style>
  :root {
    --brand-blue: #0a5191;
    --light-blue: #2e86c1;
    --ink: #1d1d1b;
    --paper: #ffffff;
    --backdrop: #eeeeee;
  }
  * { margin: 0; padding: 0; box-sizing: border-box; }
  html, body {
    width: 1200px; height: 948px; overflow: hidden;
    background: var(--backdrop);
    font-family: "Outfit", sans-serif;
  }
  .card {
    position: absolute; left: 0; top: 51px;
    width: 1630px; height: 1148px;
    background: var(--paper);
    transform: scale(0.73620);
    transform-origin: 0 0;
    overflow: hidden;
  }
  .card-shapes { position: absolute; inset: 0; width: 1630px; height: 1148px; }
  .text { position: absolute; line-height: 1; white-space: nowrap; }
  .headline {
    left: 175px; top: 90px; font-size: 84px; font-weight: 700;
    color: var(--paper); letter-spacing: 1px;
  }
  .offer {
    left: 69px; top: 280px; font-size: 63px; font-weight: 700;
    line-height: 64px; color: var(--brand-blue);
  }
  .receive {
    left: 67px; top: 445px; font-size: 92px; font-weight: 800;
    color: var(--ink); letter-spacing: -1px;
  }
  .currency {
    left: 62px; top: 572px; font-size: 170px; font-weight: 800; color: var(--ink);
  }
  .amount {
    left: 185px; top: 554px; font-size: 305px; font-weight: 800;
    color: var(--brand-blue); letter-spacing: -6px;
  }
  .phone {
    left: 155px; top: 891px; font-size: 90px; font-weight: 600; color: var(--ink);
  }
  .email, .web {
    left: 155px; font-size: 44px; font-weight: 500; color: var(--ink); letter-spacing: 1px;
  }
  .email { top: 999px; }
  .web { top: 1050px; }
  .person-name {
    right: 46px; top: 930px; font-size: 52px; font-weight: 700; color: var(--paper);
  }
  .person-role {
    right: 46px; top: 1055px; font-size: 44px; font-weight: 700; color: var(--paper);
  }
  .company-name {
    left: 1010px; top: 82px; font-size: 46px; font-weight: 700;
    line-height: 54px; color: var(--brand-blue);
  }
</style>
</head>
<body>
<section class="card">
  <svg class="card-shapes" viewBox="0 0 1630 1148" xmlns="http://www.w3.org/2000/svg">
    <defs>
      <linearGradient id="portraitTone" x1="0" y1="0" x2="0" y2="1">
        <stop offset="0" stop-color="#b48e78"/>
        <stop offset="0.45" stop-color="#d8b8a3"/>
        <stop offset="0.7" stop-color="#e9e9ee"/>
        <stop offset="1" stop-color="#2a2c3a"/>
      </linearGradient>
    </defs>

    <path class="banner" d="M0 38 H952 Q890 133 942 229 H0 Z" fill="var(--brand-blue)"/>

    <circle cx="1750" cy="1200" r="921" fill="var(--brand-blue)"/>
    <circle cx="1750" cy="1200" r="891" fill="var(--paper)"/>
    <circle cx="1750" cy="1200" r="856" fill="var(--brand-blue)"/>

    <rect class="portrait" x="1060" y="205" width="570" height="700" rx="60"
          fill="url(#portraitTone)" role="img"
          aria-label="Portrait photo of Markus Brennholt in a dark suit and white shirt"/>

    <path d="M992 1013 Q1040 899 1130 899 H1630 V1013 Z" fill="var(--light-blue)"/>
    <path d="M702 1148 Q790 1013 960 1013 H1630 V1148 Z" fill="var(--ink)"/>

    <g class="icon-thumb" fill="none" stroke="var(--paper)" stroke-width="6" stroke-linejoin="round" stroke-linecap="round">
      <path d="M120 73 V90 M95 84 L105 96 M145 84 L135 96"/>
      <rect x="71" y="128" width="22" height="42" rx="3"/>
      <path d="M93 132 L110 112 Q116 100 118 105 Q124 112 118 128 H142 Q150 130 146 140 Q152 146 145 152 Q150 160 142 164 Q146 172 136 172 H100 Q94 170 93 166 Z"/>
    </g>

    <path d="M80 916 Q76 920 79 930 Q86 950 104 960 Q112 964 118 958 L122 952 Q124 946 118 944 L108 940 Q103 939 100 944 Q92 940 88 930 Q93 927 92 922 L88 912 Q86 906 80 910 Z"
          fill="var(--brand-blue)"/>
    <g fill="none" stroke="var(--brand-blue)" stroke-width="4" stroke-linejoin="round">
      <rect x="89" y="1019" width="33" height="22" rx="2" fill="var(--brand-blue)"/>
      <path d="M89 1020 L105 1033 L122 1020" stroke="var(--paper)" stroke-width="3"/>
    </g>
    <path d="M91 1066 L118 1077 L107 1081 L117 1093 L112 1097 L102 1085 L96 1094 Z" fill="var(--brand-blue)"/>
  </svg>

  <h1 class="text headline">RECOMMEND ME!</h1>
  <p class="text offer">FOR EVERY SUCCESSFUL REAL<br>ESTATE FINANCING REFERRAL</p>
  <p class="text receive">YOU WILL RECEIVE</p>
  <span class="text currency">€</span>
  <span class="text amount">750</span>

  <p class="text phone">0676-512 4860</p>
  <p class="text email">office@die-brennholt.at</p>
  <p class="text web">www.die-brennholt.at</p>

  <p class="text company-name">Brennholt<br>Finanzberatung</p>

  <p class="text person-name">MARKUS BRENNHOLT</p>
  <p class="text person-role">GRÜNDER UND GESCHÄFTSFÜHRER</p>
</section>
</body>
</html>
```